New company branded Power Point Template for presentations

We would like to have a clean and professional PowerPoint template made for our rebranding effort. It will be for our main company (Kelvanorix) and will be used for both general introductory presentations and more technical industry related webinar and in-person presentations. We are a company in the manufacturing space working primarily in automotive. We provide simulation services to optimize production and softwares to allow users to do the same for themselves. The template needs to be easy to modify (even for novice users). I would like a good cover slide, content slides with common title / logo / etc. and a Q&A slide along with a final slide "Thank you" of similar. I have included our brand style guide in a high res pdf. Its images should be sufficient but please let me know if that is not the case.

```html
<!DOCTYPE html>
<html lang="en">
<head>
<meta charset="utf-8">
<title>Kelvanorix Presentation Template</title>
<link rel="stylesheet" href="https://fonts.googleapis.com/css2?family=Montserrat:ital,wght@0,400;0,500;0,600;0,700;0,800;1,400&display=swap">
<style>
  :root {
    --stage: #003455;
    --paper: #f7f8f8;
    --teal: #1599ad;
    --teal-line: #2fb3c8;
    --navy: #0b2a44;
    --deep: #0a3556;
    --gold: #eaa900;
    --grey: #5b6670;
    --faint: #dfe6ec;
  }
  * { margin: 0; padding: 0; box-sizing: border-box; }
  html, body { width: 1200px; height: 1001px; overflow: hidden; background: var(--stage); }
  body { position: relative; font-family: "Montserrat", sans-serif; }

  .slide {
    position: absolute; width: 651px; height: 366px;
    transform: scale(0.8); transform-origin: 0 0;
    background: var(--paper); overflow: hidden;
    box-shadow: 0 22px 20px -14px rgba(0,0,0,0.45);
  }
  .slide--cover { left: 65.6px; top: 193.6px; }
  .slide--content { left: 613.6px; top: 193.6px; }
  .slide--questions { left: 65.6px; top: 549.6px; }
  .slide--thanks { left: 613.6px; top: 549.6px; background: var(--deep); }

  .deco { position: absolute; inset: 0; width: 651px; height: 366px; }

  .brand { position: absolute; display: flex; align-items: center; gap: 9px; }
  .brand__mark { width: 36px; height: 36px; background: var(--teal); }
  .brand__name { font-weight: 700; font-size: 18px; letter-spacing: 2px; color: var(--navy); }
  .brand--cover { left: 418px; top: 167px; }
  .brand--thanks { left: 270px; top: 70px; gap: 6px; }
  .brand--thanks .brand__mark { width: 22px; height: 22px; }
  .brand--thanks .brand__name { font-size: 12px; letter-spacing: 1px; color: #fff; }

  .corner-mark { position: absolute; width: 33px; height: 33px; background: var(--teal); }
  .slide--content .corner-mark { left: 574px; top: 37px; }
  .slide--questions .corner-mark { left: 574px; top: 37px; }

  .social { position: absolute; left: 499px; top: 39px; display: flex; gap: 10px; }
  .social__dot { width: 14px; height: 14px; border-radius: 50%; background: var(--teal); }

  .site-url {
    position: absolute; right: 61px; top: 322px;
    font-size: 8px; font-weight: 700; letter-spacing: 1.6px; color: var(--teal);
  }

  .qa__title {
    position: absolute; left: 0; right: 0; top: 55px; text-align: center;
    font-size: 27px; font-weight: 700; color: var(--teal); letter-spacing: 0.3px;
  }
  .qa__subtitle {
    position: absolute; left: 0; right: 0; top: 91px; text-align: center;
    font-size: 8.5px; font-style: italic; color: var(--gold);
  }
  .faq { position: absolute; width: 278px; display: flex; gap: 9px; }
  .faq--industries { left: 59px; top: 121px; }
  .faq--support { left: 341px; top: 121px; }
  .faq--software { left: 59px; top: 205px; }
  .faq--demo { left: 341px; top: 205px; }
  .faq__icon {
    flex: none; width: 55px; height: 55px; background: var(--gold);
    display: flex; align-items: center; justify-content: center;
  }
  .faq__heading { font-size: 11.5px; font-weight: 700; color: var(--teal); margin-top: 1px; letter-spacing: 0.2px; }
  .faq__text { font-size: 6.6px; line-height: 1.5; color: #3b4750; margin-top: 5px; text-align: justify; letter-spacing: -0.15px; }

  .qa__closing {
    position: absolute; left: 0; right: 0; top: 293px; text-align: center;
    font-size: 14.5px; font-weight: 700; color: var(--teal);
  }
  .qa__note {
    position: absolute; left: 0; right: 0; top: 317px; text-align: center;
    font-size: 8.6px; font-style: italic; color: var(--grey);
  }

  .thanks__photo { position: absolute; inset: 0; }
  .thanks__title {
    position: absolute; left: 0; right: 0; top: 163px; text-align: center;
    font-size: 43px; font-weight: 800; color: #fff; letter-spacing: 0.5px;
  }
</style>
</head>
<body>

<!-- Cover slide -->
<section class="slide slide--cover">
  <svg class="deco" viewBox="0 0 651 366">
    <defs>
      <linearGradient id="coverPhoto" x1="0" y1="0" x2="1" y2="1">
        <stop offset="0" stop-color="#0d4f78"/>
        <stop offset="0.5" stop-color="#1877a3"/>
        <stop offset="1" stop-color="#0a3a5c"/>
      </linearGradient>
    </defs>
    <path d="M55 0 H245 Q290 0 290 55 V113 Z" fill="var(--gold)"/>
    <path d="M0 30 L290 165 V282 L160 366 H0 Z" fill="url(#coverPhoto)" role="img" aria-label="Blue-toned photo of a CNC milling machine cutting metal"/>
    <path d="M0 148 L180 236 L118 264 L0 206 Z" fill="var(--paper)"/>
    <path d="M0 20 L300 160" stroke="#fff" stroke-width="1.2"/>
    <path d="M0 172 L130 236" stroke="#fff" stroke-width="1"/>
    <g fill="none" stroke="var(--teal-line)" stroke-width="0.8">
      <path d="M0 0 L295 140 Q312 150 312 170 V300 L196 366"/>
      <path d="M20 0 L305 135 Q320 145 320 165 V318 L230 366"/>
      <path d="M402 0 V38 Q402 52 420 60 L651 168"/>
      <path d="M410 0 V32 Q410 46 428 54 L651 158"/>
    </g>
  </svg>
  <div class="social">
    <span class="social__dot"></span><span class="social__dot"></span><span class="social__dot"></span><span class="social__dot"></span>
  </div>
  <div class="brand brand--cover"><span class="brand__mark"></span><span class="brand__name">KELVANORIX</span></div>
  <div class="site-url">KELVANORIX.COM</div>
</section>

<!-- Content slide -->
<section class="slide slide--content">
  <svg class="deco" viewBox="0 0 651 366">
    <g fill="none" stroke="var(--faint)" stroke-width="0.8">
      <path d="M0 0 L300 145 Q318 155 318 175 V300 L200 366"/>
      <path d="M0 10 L305 158 Q312 165 312 185 V325 L240 366"/>
      <path d="M402 0 V38 Q402 52 420 60 L651 168"/>
      <path d="M410 0 V32 Q410 46 428 54 L651 158"/>
      <path d="M0 175 L130 238"/>
    </g>
  </svg>
  <span class="corner-mark"></span>
  <div class="site-url">KELVANORIX.COM</div>
</section>

<!-- Questions slide -->
<section class="slide slide--questions">
  <svg class="deco" viewBox="0 0 651 366">
    <g fill="none" stroke="var(--faint)" stroke-width="0.8">
      <path d="M0 5 L300 150 Q318 160 318 180 V300 L200 366"/>
      <path d="M402 0 V38 Q402 52 420 60 L651 168"/>
      <path d="M0 340 L60 366"/>
    </g>
  </svg>
  <span class="corner-mark"></span>
  <h2 class="qa__title">ANY QUESTIONS?</h2>
  <p class="qa__subtitle">We're here to clarify and support your success.</p>

  <div class="faq faq--industries">
    <div class="faq__icon">
      <svg width="34" height="34" viewBox="0 0 34 34" fill="#fff">
        <circle cx="17" cy="17" r="5"/>
        <circle cx="17" cy="6" r="5"/><circle cx="17" cy="28" r="5"/>
        <circle cx="6" cy="17" r="5"/><circle cx="28" cy="17" r="5"/>
        <circle cx="9.5" cy="9.5" r="4.5"/><circle cx="24.5" cy="9.5" r="4.5"/>
        <circle cx="9.5" cy="24.5" r="4.5"/><circle cx="24.5" cy="24.5" r="4.5"/>
        <circle cx="17" cy="17" r="2.5" fill="var(--gold)"/>
      </svg>
    </div>
    <div>
      <h3 class="faq__heading">INDUSTRIES WE SERVE</h3>
      <p class="faq__text">Our simulation and optimization tools are especially valuable for the automotive, aerospace, and industrial manufacturing sectors. These industries demand high precision, efficiency, and speed—exactly what our technology delivers.</p>
    </div>
  </div>

  <div class="faq faq--support">
    <div class="faq__icon">
      <svg width="34" height="34" viewBox="0 0 34 34" fill="none" stroke="#fff" stroke-width="1.8">
        <path d="M7 19 V15 A10 10 0 0 1 27 15 V19"/>
        <rect x="5" y="17" width="5" height="9" rx="2"/>
        <rect x="24" y="17" width="5" height="9" rx="2"/>
        <path d="M26 26 Q26 30 20 30 H17"/>
      </svg>
    </div>
    <div>
      <h3 class="faq__heading">ONGOING SUPPORT</h3>
      <p class="faq__text">Our platform was designed to integrate easily into existing production environments. It supports common file formats and can be adapted to specific workflows, reducing the need for major infrastructure changes.</p>
    </div>
  </div>

  <div class="faq faq--software">
    <div class="faq__icon">
      <svg width="36" height="34" viewBox="0 0 36 34" fill="#fff">
        <rect x="2" y="4" width="32" height="21" rx="5"/>
        <rect x="9" y="10" width="18" height="8" fill="var(--gold)"/>
        <rect x="14" y="25" width="8" height="5"/>
        <rect x="10" y="29" width="16" height="3" rx="1"/>
      </svg>
    </div>
    <div>
      <h3 class="faq__heading">SOFTWARE COMPATIBILITY</h3>
      <p class="faq__text">After implementation, our team offers comprehensive technical support, including regular updates, performance monitoring, and direct access to engineers and training resources. You're never left on your own.</p>
    </div>
  </div>

  <div class="faq faq--demo">
    <div class="faq__icon">
      <svg width="34" height="34" viewBox="0 0 34 34" fill="none" stroke="#fff">
        <circle cx="17" cy="17" r="13" stroke-width="4"/>
        <circle cx="17" cy="17" r="6" stroke-width="4"/>
      </svg>
    </div>
    <div>
      <h3 class="faq__heading">DEMO OR TRIAL OPTIONS</h3>
      <p class="faq__text">Yes — we encourage potential clients to request a personalized demo or pilot program. This helps you evaluate real-world benefits before making a long-term decision.</p>
    </div>
  </div>

  <p class="qa__closing">Still have questions?</p>
  <p class="qa__note">Reach out to our team — we're happy to help with anything else you need.</p>
</section>

<!-- Thank-you slide -->
<section class="slide slide--thanks">
  <svg class="thanks__photo" viewBox="0 0 651 366" role="img" aria-label="Dark blue-toned photo of a lathe machining metal with sparks">
    <defs>
      <radialGradient id="thanksPhoto" cx="0.4" cy="0.6" r="0.8">
        <stop offset="0" stop-color="#1d5479"/>
        <stop offset="0.6" stop-color="#0d3a5c"/>
        <stop offset="1" stop-color="#072b47"/>
      </radialGradient>
    </defs>
    <rect width="651" height="366" fill="url(#thanksPhoto)"/>
  </svg>
  <svg class="deco" viewBox="0 0 651 366">
    <g fill="none" stroke="rgba(255,255,255,0.55)" stroke-width="0.8">
      <path d="M0 5 L300 150 Q318 160 318 180 V300 L195 366"/>
      <path d="M0 18 L305 165 Q312 172 312 190 V320 L245 366"/>
      <path d="M402 0 V38 Q402 52 420 60 L651 168"/>
      <path d="M410 0 V32 Q410 46 428 54 L651 158"/>
      <path d="M0 165 L130 235"/>
    </g>
  </svg>
  <div class="brand brand--thanks"><span class="brand__mark"></span><span class="brand__name">KELVANORIX</span></div>
  <h2 class="thanks__title">THANK YOU</h2>
</section>

</body>
</html>
```